Design our next "BOLD HORIZON" print. Size 12x36 Horizontal.

I am looking for a poster design with the text "Bold Horizon" . The print size will be a 12x36 inches.(Horizontal) It should have the American flag used throughout the design. I am looking for a very proud feeling. Font can be creative but instantly readable. The design can be old world feel and can also use the deep reds and navy blues.The image does not have to be just the flag and text. It can contain other patriotic symbols. Can also have a grungy feel. I have enclosed our last "Bold Horizon " piece for your reference. We are hoping we can get one even better. Thank You.

• Should Not be like the image example I enclosed. It's just a reference. We need something that is new and different. Plain White text.

```html
<!DOCTYPE html>
<html lang="en">
<head>
<meta charset="utf-8">
<title>Bold Horizon – Patriotic Print</title>
<link rel="stylesheet" href="https://fonts.googleapis.com/css2?family=Black+Ops+One&display=swap">
<style>
  :root {
    --sky-blue: #3ab4ea;
    --bright-blue: #1f8fd6;
    --navy: #232a8a;
    --deep-navy: #1a1f6b;
    --maroon: #5a1c26;
    --plum: #4a2a45;
    --slate-teal: #3f819e;
    --deep-teal: #133543;
    --pale-star: #cfe9f7;
    --ink: #ffffff;
  }
  html, body {
    margin: 0;
    padding: 0;
    width: 1200px;
    height: 400px;
    overflow: hidden;
    background: var(--slate-teal);
  }
  .poster {
    position: relative;
    width: 1200px;
    height: 400px;
    overflow: hidden;
  }
  .poster-art {
    position: absolute;
    inset: 0;
    display: block;
  }
  .headline {
    font-family: "Black Ops One", "Arial Black", sans-serif;
    fill: var(--ink);
  }
</style>
</head>
<body>
<main class="poster">
  <svg class="poster-art" width="1200" height="400" viewBox="0 0 1200 400" xmlns="http://www.w3.org/2000/svg">
    <defs>
      <linearGradient id="flag-wash" x1="0" y1="0" x2="1" y2="0">
        <stop offset="0" stop-color="var(--bright-blue)"/>
        <stop offset="0.35" stop-color="var(--sky-blue)"/>
        <stop offset="0.6" stop-color="var(--slate-teal)"/>
        <stop offset="1" stop-color="var(--slate-teal)"/>
      </linearGradient>
      <linearGradient id="torch-tone" x1="0" y1="0" x2="1" y2="1">
        <stop offset="0" stop-color="#9fd8f2" stop-opacity="0.5"/>
        <stop offset="1" stop-color="#2a5f8f" stop-opacity="0.4"/>
      </linearGradient>
      <polygon id="star" points="0,-50 11.8,-16.2 47.6,-15.5 19,6.2 29.4,40.5 0,20 -29.4,40.5 -19,6.2 -47.6,-15.5 -11.8,-16.2"/>
    </defs>

    <!-- painted flag backdrop -->
    <rect class="flag-backdrop" width="1200" height="400" fill="url(#flag-wash)"/>

    <!-- navy canton brushed across the left -->
    <g class="canton-wash" fill="var(--navy)">
      <path d="M0 0 L300 0 C270 40 230 60 240 110 C200 140 150 130 120 190 C80 230 40 220 0 260 Z" opacity="0.85"/>
      <path d="M0 280 C60 260 120 290 170 300 L140 400 L0 400 Z" fill="var(--deep-navy)" opacity="0.8"/>
      <path d="M380 0 L560 0 C540 40 470 40 430 70 C400 50 390 30 380 0 Z" opacity="0.55"/>
    </g>

    <!-- star field -->
    <g class="star-field">
      <use href="#star" transform="translate(70 60) scale(0.9) rotate(-12)" fill="var(--deep-navy)"/>
      <use href="#star" transform="translate(180 110) scale(0.8) rotate(8)" fill="var(--pale-star)" opacity="0.55"/>
      <use href="#star" transform="translate(120 150) scale(0.55) rotate(20)" fill="var(--navy)"/>
      <use href="#star" transform="translate(40 200) scale(0.7) rotate(-5)" fill="var(--pale-star)" opacity="0.45"/>
      <use href="#star" transform="translate(260 40) scale(0.6) rotate(15)" fill="var(--pale-star)" opacity="0.5"/>
      <use href="#star" transform="translate(350 20) scale(0.5)" fill="var(--deep-navy)" opacity="0.8"/>
      <use href="#star" transform="translate(500 130) scale(0.55) rotate(-10)" fill="var(--navy)" opacity="0.8"/>
      <use href="#star" transform="translate(60 320) scale(0.9) rotate(6)" fill="var(--deep-navy)"/>
      <use href="#star" transform="translate(150 270) scale(0.45) rotate(-18)" fill="var(--pale-star)" opacity="0.5"/>
      <use href="#star" transform="translate(30 380) scale(0.5)" fill="var(--pale-star)" opacity="0.4"/>
      <use href="#star" transform="translate(1130 40) scale(0.6) rotate(10)" fill="var(--pale-star)" opacity="0.5"/>
    </g>

    <!-- pale grunge wash top centre-right -->
    <g class="grunge-wash" fill="var(--pale-star)">
      <path d="M690 0 L900 0 C880 30 840 60 800 70 C760 60 720 40 690 0 Z" opacity="0.35"/>
      <path d="M30 110 C80 100 140 120 190 115 L185 125 C140 130 80 112 30 122 Z" opacity="0.6"/>
      <path d="M200 230 C240 220 290 228 330 222 L328 230 C290 236 240 230 200 240 Z" opacity="0.5"/>
      <path d="M1150 100 C1170 80 1190 70 1200 65 L1200 170 C1180 150 1160 130 1150 100 Z" opacity="0.3"/>
    </g>

    <!-- plum grunge top right -->
    <path class="grunge-plum" d="M820 0 L1200 0 L1200 60 C1120 80 1040 60 960 72 C900 78 860 70 840 50 C830 30 820 15 820 0 Z"
          fill="var(--plum)" opacity="0.85"/>

    <!-- sweeping stripe bands -->
    <g class="stripe-bands" fill="var(--maroon)">
      <path d="M860 60 C960 55 1080 62 1200 70 L1200 92 C1080 85 960 80 860 84 Z"/>
      <path d="M540 168 C720 150 960 148 1200 158 L1200 222 C980 205 740 210 560 226 Z"/>
      <path d="M160 318 C450 290 800 280 1200 296 L1200 350 C820 330 480 340 180 380 Z"/>
      <path d="M0 372 C300 356 650 360 1000 372 L1000 400 L0 400 Z" opacity="0.9"/>
    </g>
    <path class="corner-shadow" d="M1000 400 C1070 350 1140 330 1200 325 L1200 400 Z" fill="var(--deep-teal)"/>

    <!-- torch illustration area -->
    <path class="torch-illustration" d="M300 10 L345 120 L350 175 L260 250 L150 330 L128 318 L215 200 L230 130 Z"
          fill="url(#torch-tone)" role="img" aria-label="Line drawing of the Statue of Liberty torch"/>

    <!-- headline -->
    <text class="headline headline-top" x="612" y="180" font-size="182"
          text-anchor="middle" textLength="392" lengthAdjust="spacingAndGlyphs">Bold</text>
    <text class="headline headline-bottom" x="615" y="336" font-size="182"
          text-anchor="middle" textLength="818" lengthAdjust="spacingAndGlyphs">Horizon</text>
  </svg>
</main>
</body>
</html>
```